Business card for a shipping supplies business

Needing a business card design. Please see the logo. The logo with the white font should be used if there is a dark background.

We are looking for the following info on the card. Please see the sample info. We will need the info to be changed with a few different employee names and info but all will use the same template.

Business Name: The Crate Heron
Employee Name : Marcus Delaney
Position: Account Manager
Address: 4827 W. Ridge 418 S.
Cedar Hollow, OK 73948
email: Marcus@thecrateheron.example
telephone: 855-619-2740 x 207
website: www.getparcelkits.example

Target Market(s)

Businesses who ship products for online sales

Industry/Entity Type

Cardboard

Contact Information for Business Card

Name, title, address, website, logo, telephone number

Font styles to use
Sans Serif

Colors
EE7325
F08F49
F5BC92
FAE3D3
FDF4ED

Requirements
Must have
• Logo on back of card. Clean look, just logo, website address

```html
<!DOCTYPE html>
<html lang="en">
<head>
<meta charset="utf-8">
<title>The Crate Heron – Business Card</title>
<link rel="stylesheet" href="https://fonts.googleapis.com/css2?family=Ubuntu:wght@400;500;700&display=swap">
<style>
  :root {
    --orange: #EE7325;
    --orange-soft: #F08F49;
    --card: #1d1d1d;
    --card-edge: #050505;
    --backdrop: #2a2a2a;
    --white: #f4f4f4;
  }
  * { margin: 0; padding: 0; box-sizing: border-box; }
  html, body { width: 1200px; height: 900px; overflow: hidden; }
  body {
    background: var(--backdrop);
    font-family: "Ubuntu", sans-serif;
    display: flex;
    flex-direction: column;
    align-items: center;
    justify-content: center;
    gap: 36px;
  }
  .card {
    position: relative;
    width: 700px;
    height: 400px;
    background: radial-gradient(ellipse at 50% 40%, #252525 0%, var(--card) 70%);
    border: 12px solid var(--card-edge);
    color: var(--white);
  }
  /* Front: contact side */
  .identity {
    position: absolute;
    left: 120px;
    top: 150px;
  }
  .identity .name {
    color: var(--orange);
    font-size: 30px;
    font-weight: 500;
    letter-spacing: 0.5px;
  }
  .identity .title {
    font-size: 17px;
    margin-top: 4px;
    padding-left: 34px;
  }
  .contacts {
    position: absolute;
    left: 372px;
    top: 92px;
    list-style: none;
    font-size: 16px;
  }
  .contacts li {
    display: flex;
    align-items: center;
    gap: 12px;
    height: 32px;
  }
  .contacts svg { width: 14px; height: 14px; fill: var(--orange); flex: none; }
  .pin {
    position: absolute;
    left: 468px;
    top: 236px;
    width: 16px;
    height: 20px;
    fill: var(--orange);
  }
  .address {
    position: absolute;
    left: 0;
    right: 0;
    bottom: 42px;
    text-align: center;
    font-size: 17px;
    padding-left: 60px;
  }
  /* Back: brand side */
  .brand {
    position: absolute;
    left: 0;
    right: 0;
    top: 120px;
    display: flex;
    align-items: center;
    justify-content: center;
    gap: 16px;
  }
  .brand-mark {
    width: 34px;
    height: 34px;
    background: var(--orange);
  }
  .brand-name {
    font-size: 44px;
    font-weight: 700;
    color: var(--white);
  }
  .site {
    position: absolute;
    left: 0;
    right: 0;
    top: 258px;
    text-align: center;
    font-size: 19px;
    font-weight: 500;
    letter-spacing: 2px;
  }
  .site .domain { color: var(--orange); }
</style>
</head>
<body>
  <section class="card card-front">
    <div class="identity">
      <div class="name">Marcus Delaney</div>
      <div class="title">Account Manager</div>
    </div>
    <ul class="contacts">
      <li>
        <svg viewBox="0 0 16 16" aria-hidden="true"><path d="M3.5 1l3 3-1.8 1.8a9 9 0 0 0 5.5 5.5L12 9.5l3 3-2 2C6.5 14.5 1.5 9.5 1.5 3z"/></svg>
        <span>855-619-2740 x 207</span>
      </li>
      <li>
        <svg viewBox="0 0 16 16" aria-hidden="true"><path d="M1 3h14v2L8 9 1 5z M1 7l7 4 7-4v6H1z"/></svg>
        <span>Marcus@thecrateheron.example</span>
      </li>
      <li>
        <svg viewBox="0 0 16 16" aria-hidden="true"><circle cx="8" cy="8" r="7"/></svg>
        <span>www.getparcelkits.example</span>
      </li>
    </ul>
    <svg class="pin" viewBox="0 0 16 20" aria-hidden="true"><path d="M8 0a7 7 0 0 1 7 7c0 5-7 13-7 13S1 12 1 7a7 7 0 0 1 7-7zm0 4.5a2.5 2.5 0 1 0 0 5 2.5 2.5 0 0 0 0-5z"/></svg>
    <p class="address">4827 W. Ridge 418 S. Cedar Hollow, OK 73948</p>
  </section>

  <section class="card card-back">
    <div class="brand">
      <span class="brand-mark"></span>
      <span class="brand-name">The Crate Heron</span>
    </div>
    <p class="site">www.<span class="domain">getparcelkits</span>.example</p>
  </section>
</body>
</html>
```